Equine Horse Employment site

We need to redesign the layout of Stablemark Hire.co.uk

It will offer Job seekers and Employers the place to look for a job, and look for a candidate.

The logical format needs to be improved and the layout must look highly visually appealing.

It needs to be incredibly simple to use and one click access to any part of the site.

The homepage must convey the following

- Log in and register areas
- Current Job Listings
- Current CV's
- Exclusive Service Club button
- Search box to allow simple searching for Jobs or CVs

We need PSD layouts for Homepage, Job listing Page, CV listing Page, Job Profile and CV Profile. This job is for the design of 5 PSD screens.

Generic page for ancillary page such as about, contact and news.

The biggest competitor is PaddockPost.com

Please ask us any questions and please be prepared to make changes, as we are very particular.

More work will be provided to the winning designer.

thanks

• It must not look cheap or like a job board, it has to have character and feel friendly, and inviting. Please do not submit poor designs that look like a job board, as they will be rejected instantly.

thanks

```html
<!DOCTYPE html>
<html lang="en">
<head>
<meta charset="utf-8">
<title>Stablemark Hire – Equestrian Recruitment Specialists</title>
<link href="https://fonts.googleapis.com/css2?family=Source+Sans+3:ital,wght@0,400;0,600;0,700;1,400&display=swap" rel="stylesheet">
<style>
:root{
  --maroon:#4a1812;
  --maroon-dark:#3b120e;
  --green:#7c9c25;
  --green-text:#6f9420;
  --field:#ececec;
  --line:#e2e2e2;
  --text:#333;
  --muted:#555;
  --white:#fff;
}
*{box-sizing:border-box;margin:0;padding:0}
html,body{width:835px;height:1200px;overflow:hidden;background:var(--white)}
body{position:relative;font-family:"Source Sans 3",Arial,sans-serif;color:var(--text)}
.abs{position:absolute}
.top-rule{left:0;top:0;width:835px;height:5px;background:var(--maroon)}
.account-tab{left:658px;top:0;width:128px;height:28px;background:var(--maroon);border-radius:0 0 8px 8px;color:#ddd;font-size:9px;display:flex;align-items:center;justify-content:center;gap:6px}
.account-tab b{color:var(--white);font-weight:600}
.account-tab span{opacity:.5}
.brand{left:40px;top:62px;font-size:22px;font-weight:600;color:var(--maroon);letter-spacing:.5px}
.brand-dot{display:inline-block;width:12px;height:12px;border-radius:50%;background:var(--maroon);margin-right:6px;vertical-align:1px}
.brand-tag{left:71px;top:90px;font-size:7.5px;font-weight:600;color:var(--maroon)}
.social{left:708px;top:43px;display:flex;gap:8px}
.social i{display:block;width:18px;height:18px;border-radius:50%;background:var(--green)}
.main-nav{left:380px;top:86px;display:flex;align-items:center;font-size:12px;color:#3a2a28}
.main-nav a{color:inherit;text-decoration:none}
.main-nav .sep{width:1px;height:26px;background:#888;transform:skewX(-20deg);margin:0 12px}
.hero{left:43px;top:118px;width:752px;height:262px;background:linear-gradient(110deg,#c9d8e8 0%,#7d98b8 35%,#2d3540 55%,#a9c0da 75%,#dfe8f2 100%)}
.search-box{left:526px;top:180px;width:256px;height:150px;background:var(--white);border-radius:3px;box-shadow:0 1px 4px rgba(0,0,0,.2);padding:12px 16px}
.search-box h2{font-size:13.5px;font-weight:400;color:#222;margin-bottom:9px}
.field{height:24px;background:var(--field);border-radius:2px;font-size:9.5px;font-style:italic;color:#444;padding:6px 9px;margin-bottom:9px}
.search-row{display:flex;justify-content:space-between;align-items:flex-start}
.btn-green{display:inline-block;background:var(--green);color:var(--white);font-weight:600;border:1px solid #5d7a14;border-radius:2px}
.search-row .btn-green{font-size:11px;padding:5px 10px}
.search-row small{font-size:9px;color:#555;margin-top:-3px}
.panel{border:1px solid var(--line);background:var(--white)}
.jobs{left:41px;top:394px;width:551px;height:328px}
.panel-head{height:35px;color:var(--white);font-size:13.5px;padding:8px 15px}
.head-maroon{background:var(--maroon)}
.head-green{background:var(--green);height:32px;padding-top:7px}
.job-grid{position:absolute;left:16px;top:50px;display:grid;grid-template-columns:repeat(4,136px);row-gap:22px}
.job h3{font-size:10.5px;font-weight:400;color:var(--green-text)}
.job .place{font-size:10px;color:#222;margin-top:1px}
.job p{font-size:8.4px;line-height:11.5px;color:#444;margin-top:3px;width:120px}
.job .posted{font-size:8.5px;font-weight:600;margin-top:3px}
.btn-maroon{display:inline-block;background:var(--maroon);color:var(--white);font-size:8.5px;padding:3px 8px;border-radius:2px;margin-top:8px}
.view-more{left:57px;top:692px;font-size:10px;color:var(--maroon);font-weight:600}
.cv{left:41px;top:727px;width:551px;height:218px}
.cv-grid{position:absolute;left:30px;top:48px;display:grid;grid-template-columns:repeat(3,174px);row-gap:20px}
.cv-item{display:flex;gap:10px}
.avatar{width:40px;height:48px;border-radius:50% 50% 40% 40%;background:radial-gradient(circle at 50% 25%,#f3c267 0 26%,transparent 27%),linear-gradient(#fff 45%,#5d8fd6 46%);flex:none}
.cv-item h3{font-size:10px;font-weight:400;color:var(--green-text)}
.cv-item .role{font-size:10px;color:#222;margin-top:1px}
.cv-item p{font-size:8.4px;line-height:11.5px;color:#444;margin-top:2px;width:100px}
.login{left:599px;top:394px;width:196px;height:128px;padding:10px 14px}
.side-title{font-size:13.5px;color:var(--green-text);font-weight:400}
.login .field{height:21px;font-size:9px;padding:5px 10px;margin:0 0 8px 0;background:#eeeded}
.login .btn-green{font-size:9.5px;padding:3px 10px}
.promo{left:599px;width:196px;color:var(--white);padding:10px 18px}
.promo h2{font-size:13.5px;font-weight:400}
.promo p{font-size:8.4px;line-height:12.5px;margin-top:3px}
.register{top:529px;height:97px;background:var(--maroon)}
.register .btn-green{font-size:9px;padding:3px 9px;margin-top:8px}
.club{top:631px;height:91px;background:var(--green)}
.club p{color:#e8f0d0}
.club .btn-dark{display:inline-block;background:var(--maroon-dark);font-size:9px;font-weight:600;padding:3px 9px;margin-top:8px;border-radius:2px}
.testimonial{left:599px;top:731px;width:196px;height:213px;padding:10px 15px}
.testimonial h2{font-size:13.5px;font-weight:400;color:#222}
.quote-photo{float:left;width:54px;height:55px;background:linear-gradient(#a88070,#e2bfa8);margin:6px 8px 3px 2px}
.testimonial h3{font-size:10px;font-weight:400;color:var(--green-text);padding-top:5px}
.testimonial p{font-size:8.2px;line-height:14px;font-style:italic;color:#444}
.testimonial .author{clear:both;font-size:10px;color:var(--green-text);margin-top:10px;padding-left:5px}
.footer{left:0;top:956px;width:835px;height:244px;background:var(--maroon-dark);color:#f1e6e4}
.footer h2{font-size:11.5px;font-weight:600;color:var(--white)}
.foot-about{left:46px;top:21px;width:210px;font-size:9px;line-height:14.5px}
.foot-about p{margin-top:10px}
.foot-links{top:21px;font-size:9px;list-style:none}
.foot-links li{margin-top:9px}
.foot-links li::before{content:"›";margin-right:6px}
.foot-news{left:590px;top:21px;width:210px;font-size:9px}
.email-field{width:157px;height:19px;border-radius:10px;background:#a08e8b;color:#2b1a18;font-size:9px;padding:3px 11px;margin-top:10px}
.btn-subscribe{display:inline-block;background:#f1ecea;color:#2b1a18;font-weight:600;font-size:9.5px;padding:2px 10px;border-radius:2px;margin-top:10px;margin-left:3px}
.foot-rule{left:44px;top:179px;width:748px;height:1px;background:#5a2b26}
.copyright{left:47px;top:193px;font-size:8px;color:#bca9a5}
</style>
</head>
<body>
<div class="abs top-rule"></div>
<div class="abs account-tab"><b>Guest</b><span>|</span>Register | Log In</div>

<div class="abs brand"><span class="brand-dot"></span>Stablemark Hire</div>
<div class="abs brand-tag">Equestrian Recruitment Specialists</div>
<div class="abs social"><i></i><i></i><i></i></div>

<nav class="abs main-nav">
  <a href="#">Home</a><span class="sep"></span>
  <a href="#">About Us</a><span class="sep"></span>
  <a href="#">Employers</a><span class="sep"></span>
  <a href="#">Advertise</a><span class="sep"></span>
  <a href="#">News</a><span class="sep"></span>
  <a href="#">Resources</a>
</nav>

<div class="abs hero" role="img" aria-label="Photo of smiling business professionals in front of a glass office building"></div>
<div class="abs search-box">
  <h2>Quick Jobs Search</h2>
  <div class="field">Enter Job Type</div>
  <div class="field">Location</div>
  <div class="search-row"><span class="btn-green">FIND JOB NOW</span><small>Advanced Search</small></div>
</div>

<section class="abs panel jobs">
  <div class="panel-head head-maroon">Current Job Listings</div>
  <div class="job-grid">
    <div class="job"><h3>Full Time Barn Help</h3><div class="place">Florida</div><p>Lorem ipsum dolor sit amet, consectetuer adipiscing elit. Nam cursus.</p><div class="posted">Posted 3 hour ago</div><span class="btn-maroon">Apply now</span></div>
    <div class="job"><h3>Full Time Barn Help</h3><div class="place">Florida</div><p>Lorem ipsum dolor sit amet, consectetuer adipiscing elit. Nam cursus.</p><div class="posted">Posted 3 hour ago</div><span class="btn-maroon">Apply now</span></div>
    <div class="job"><h3>Full Time Barn Help</h3><div class="place">Florida</div><p>Lorem ipsum dolor sit amet, consectetuer adipiscing elit. Nam cursus.</p><div class="posted">Posted 3 hour ago</div><span class="btn-maroon">Apply now</span></div>
    <div class="job"><h3>Full Time Barn Help</h3><div class="place">Florida</div><p>Lorem ipsum dolor sit amet, consectetuer adipiscing elit. Nam cursus.</p><div class="posted">Posted 3 hour ago</div><span class="btn-maroon">Apply now</span></div>
    <div class="job"><h3>Full Time Barn Help</h3><div class="place">Florida</div><p>Lorem ipsum dolor sit amet, consectetuer adipiscing elit. Nam cursus.</p><div class="posted">Posted 3 hour ago</div><span class="btn-maroon">Apply now</span></div>
    <div class="job"><h3>Full Time Barn Help</h3><div class="place">Florida</div><p>Lorem ipsum dolor sit amet, consectetuer adipiscing elit. Nam cursus.</p><div class="posted">Posted 3 hour ago</div><span class="btn-maroon">Apply now</span></div>
    <div class="job"><h3>Full Time Barn Help</h3><div class="place">Florida</div><p>Lorem ipsum dolor sit amet, consectetuer adipiscing elit. Nam cursus.</p><div class="posted">Posted 3 hour ago</div><span class="btn-maroon">Apply now</span></div>
    <div class="job"><h3>Full Time Barn Help</h3><div class="place">Florida</div><p>Lorem ipsum dolor sit amet, consectetuer adipiscing elit. Nam cursus.</p><div class="posted">Posted 3 hour ago</div><span class="btn-maroon">Apply now</span></div>
  </div>
</section>
<div class="abs view-more">VIEW MORE ›</div>

<section class="abs panel cv">
  <div class="panel-head head-green">Current CV</div>
  <div class="cv-grid">
    <div class="cv-item"><div class="avatar" role="img" aria-label="Candidate avatar icon"></div><div><h3>Candidate Name</h3><div class="role">MED.</div><p>Lorem ipsum dolor sit amet, consectetuer adipiscing elit.</p></div></div>
    <div class="cv-item"><div class="avatar" role="img" aria-label="Candidate avatar icon"></div><div><h3>Candidate Name</h3><div class="role">MED.</div><p>Lorem ipsum dolor sit amet, consectetuer adipiscing elit.</p></div></div>
    <div class="cv-item"><div class="avatar" role="img" aria-label="Candidate avatar icon"></div><div><h3>Candidate Name</h3><div class="role">MED.</div><p>Lorem ipsum dolor sit amet, consectetuer adipiscing elit.</p></div></div>
    <div class="cv-item"><div class="avatar" role="img" aria-label="Candidate avatar icon"></div><div><h3>Candidate Name</h3><div class="role">MED.</div><p>Lorem ipsum dolor sit amet, consectetuer adipiscing elit.</p></div></div>
    <div class="cv-item"><div class="avatar" role="img" aria-label="Candidate avatar icon"></div><div><h3>Candidate Name</h3><div class="role">MED.</div><p>Lorem ipsum dolor sit amet, consectetuer adipiscing elit.</p></div></div>
    <div class="cv-item"><div class="avatar" role="img" aria-label="Candidate avatar icon"></div><div><h3>Candidate Name</h3><div class="role">MED.</div><p>Lorem ipsum dolor sit amet, consectetuer adipiscing elit.</p></div></div>
  </div>
</section>

<section class="abs panel login">
  <h2 class="side-title" style="margin-bottom:10px">Login / Register</h2>
  <div class="field">username</div>
  <div class="field">password</div>
  <span class="btn-green">Login</span>
</section>

<section class="abs promo register">
  <h2>Register Free Now</h2>
  <p>Lorem ipsum dolor sit amet, consectetuer adipiscing elit. Nam cursus. mattis, massa.</p>
  <span class="btn-green">REGISTER ›</span>
</section>

<section class="abs promo club">
  <h2>Exclusive Service Club</h2>
  <p>Lorem ipsum dolor sit amet, consectetuer adipiscing elit. Nam cursus. mattis, massa.</p>
  <span class="btn-dark">CLICK HERE ›</span>
</section>

<section class="abs panel testimonial">
  <h2>Testimonial</h2>
  <div class="quote-photo" role="img" aria-label="Portrait photo of a smiling client"></div>
  <h3>Tittle of Testimonial</h3>
  <p>Etiam est nunc, venenatis in, tristique eu, imperdiet ac, nisl. Cum sociis natoque penatibus et magnis dis parturient montes, nascetur ridiculus mus. In iaculis facilisis massa. Etiam eu urna. Sed porta. Suspendisse quam leo, molestie sed, luctus quis, feugiat in, pede.</p>
  <div class="author">BY AUTHOR NAME</div>
</section>

<footer class="abs footer">
  <div class="abs foot-about">
    <h2>About Company</h2>
    <p>Equestrian Jobs at Stablemark Hire. A precise way for equine job seekers and employers to conduct a search for qualified candidates and jobs.</p>
    <p>No1 in Seekly and a reach of over 500,000 users in the UK alone. Now partnered with Marketlane providing greater reach to the best talent in Europe.</p>
  </div>
  <div class="abs" style="left:302px;top:21px"><h2>Quick Links</h2></div>
  <ul class="abs foot-links" style="left:305px;top:35px">
    <li>Home</li><li>About Stablemark Hire</li><li>Equine Job Seekers</li><li>Equine Employers</li><li>Equine Industry News</li>
  </ul>
  <ul class="abs foot-links" style="left:445px;top:35px">
    <li>Equestrian Resources</li><li>Webmasters</li><li>Login</li><li>Sitemap</li>
  </ul>
  <div class="abs foot-news">
    <h2>Newslettes Subscibe</h2>
    <div style="margin-top:7px">Sign up for latest Newsletters Updates</div>
    <div class="email-field">enter email address</div>
    <span class="btn-subscribe">Subscribe</span>
  </div>
  <div class="abs foot-rule"></div>
  <div class="abs copyright">© 2012 Company Name &nbsp;|&nbsp; All right reserved</div>
</footer>
</body>
</html>
```